Lumen Kinetics Web Design Project

We need to update our web design for our company. Lumen Kinetics™ is a series of Development (Training) Programs that we deliver both for the General Public as well as Corporate Business.

Much of the content needs a refresh but we are keen to get some thoughts now on design and layout, predominantly front page. Happy to take any comments on the content if you think that is relevant as well.

We might look to move the current video clip and bring a more generic 'inspirational' clip to the front page. A good example of this is www.mindcraftoz.example.au

Our courses have a very similar market to Gerald Whitcombe type courses ... both General Public and Corporate business.

Refer our website www.lumenkinetics.example.com

Target Market(s)

General Public as well as Corporate Business. Courses are designed for all. Gerald Whitcombe would be a good 'feel' for what we do.

Industry/Entity Type

Business

Requirements
Must have
• Must have a 'leading edge' type feel to it.
Must look professional.

```html
<!DOCTYPE html>
<html lang="en">
<head>
<meta charset="utf-8">
<title>Lumen Kinetics — Home</title>
<link href="https://fonts.googleapis.com/css2?family=Alegreya:wght@400;500&family=Arimo:wght@400&display=swap" rel="stylesheet">
<style>
:root{
  --blue:#2a78b6;
  --blue-light:#3d8fcb;
  --ink:#3a3a3a;
  --muted:#6b6b6b;
  --rule:#d9d9d9;
  --hero:#3a3230;
  --hero-deep:#2c2624;
  --footer:#2a2828;
  --cyan:#2ea3d9;
  --yellow:#f2df00;
  --magenta:#e3197f;
  --white:#ffffff;
}
*{box-sizing:border-box;margin:0;padding:0}
html,body{width:1200px;height:2457px;overflow:hidden}
body{position:relative;background:var(--white);font-family:"Alegreya",Georgia,serif;color:var(--ink)}
.abs{position:absolute}
a{color:inherit;text-decoration:none}

/* header */
.brand{left:147px;top:52px;display:flex;align-items:center;gap:12px}
.brand-dot{width:22px;height:22px;border-radius:50%;background:var(--blue)}
.brand-name{font-size:40px;font-weight:500;color:var(--blue);line-height:1}
.phone{right:96px;top:52px;display:flex;align-items:center;gap:12px;font-size:20px;color:var(--ink)}
.nav{right:96px;top:106px;display:flex;font-size:14px;color:var(--muted)}
.nav a{padding:0 11px;border-left:1px solid #bbb;line-height:14px}
.nav a:first-child{border-left:0}
.nav a:last-child{padding-right:0}
.nav .current{color:var(--blue)}

/* hero */
.hero{left:0;top:158px;width:1200px;height:569px;background:linear-gradient(125deg,#453c39 0%,var(--hero) 45%,var(--hero-deep) 100%)}
.hero-title{left:115px;top:262px;width:360px;font-size:40px;line-height:46px;color:#e4dedb;font-weight:400}
.hero-sub{left:115px;top:494px;width:300px;font-size:22px;line-height:31px;color:#b8aeaa}
.video{left:491px;top:240px;width:627px;height:420px;background:#111}
.video-frame{position:absolute;left:0;top:0;width:627px;height:374px;background:linear-gradient(160deg,#cfd6de 0%,#9aa6b3 35%,#5a4f4a 70%,#2c2c34 100%)}
.video-bar{position:absolute;left:0;top:374px;width:627px;height:46px;background:#1b1b1b}
.stripe{height:7px}
.stripe span{display:inline-block;height:7px;width:284px;vertical-align:top}
.c1{background:var(--cyan)}.c2{background:var(--yellow)}.c3{background:var(--magenta)}

/* features */
.feature{width:255px}
.feature-head{display:flex;align-items:center;gap:14px}
.num{width:36px;height:36px;border-radius:50%;background:var(--blue);color:#fff;font-size:22px;display:flex;align-items:center;justify-content:center}
.feature-title{font-size:26px;color:var(--ink);font-weight:400}
.feature p{margin:12px 0 0 50px;font-size:12.5px;line-height:16px;color:var(--muted)}
.more{display:flex;align-items:center;justify-content:flex-end;gap:12px;font-size:14px;color:var(--blue)}
.go{width:14px;height:14px}

/* section headings */
.section-head{display:flex;align-items:center;gap:14px}
.section-title{font-size:22px;color:var(--blue);font-weight:400;white-space:nowrap}
.section-rule{flex:1;height:1px;background:var(--rule)}
.pager{display:flex;gap:2px}

.tabs{left:187px;top:1042px;display:flex;font-size:14px;color:var(--muted)}
.tabs span{padding:0 12px;border-left:1px solid #bbb;line-height:14px}
.tabs span:first-child{padding-left:0;border-left:0}
.tabs .on{color:var(--blue)}
.thumb{top:1100px;width:148px;height:128px}

/* training */
.course{width:258px}
.course-title{font-size:19px;color:var(--ink);font-weight:400}
.course-meta{margin-top:10px;padding:6px 0;border-top:1px solid var(--rule);border-bottom:1px solid var(--rule);display:flex;align-items:center;font-size:13px;color:var(--muted)}
.course-meta .sep{margin:0 9px;width:1px;height:13px;background:#bbb}
.course-meta .count{margin-left:auto;display:flex;align-items:center;gap:9px}
.course-img{margin-top:14px;height:120px}
.course p{margin-top:22px;font-size:12.5px;line-height:16px;color:var(--muted)}
.course .more{margin-top:18px}

/* lists & testimonials */
.links{left:184px;top:1694px;width:240px;list-style:none}
.links li{display:flex;gap:14px;font-size:13.5px;line-height:17px;color:var(--ink);margin-bottom:14px}
.links .go{flex:none;margin-top:2px}
.quote{width:240px}
.quote-mark{font-size:48px;line-height:40px;color:var(--blue)}
.quote p{margin-top:10px;font-size:12.5px;line-height:16px;color:var(--ink)}
.person{font-size:13px;color:var(--blue)}
.role{font-size:11px;color:var(--muted)}
.portrait{width:68px;height:82px}

.tweet{width:250px;display:flex;gap:14px}
.tweet-dot{flex:none;width:11px;height:11px;border-radius:50%;background:var(--blue-light);margin-top:4px}
.tweet p{font-size:12.5px;line-height:16px;color:var(--ink)}
.tweet .tag{color:var(--blue)}
.tweet .date{font-size:10.5px;color:var(--muted);margin-top:6px}

/* footer */
.footer{left:0;top:2093px;width:1200px;height:364px;background:linear-gradient(120deg,#332f30 0%,var(--footer) 40%,#1f1e1e 100%)}
.foot-title{font-size:20px;color:#fff;font-weight:400}
.foot-sans{font-family:"Arimo",Arial,sans-serif}
.foot-text{font-size:12px;line-height:15px;color:#e6e6e6}
.foot-row{display:flex;gap:14px;align-items:flex-start;font-size:13px;line-height:15px;color:#e6e6e6;margin-top:18px}
.foot-row svg{flex:none}
.social{display:flex;gap:12px}
.social span{width:30px;height:30px;border-radius:50%;border:2px solid #fff}
.foot-rule{left:188px;top:2367px;width:836px;height:1px;background:#4a4646}
.copyright{left:188px;top:2391px;font-size:13px;color:#ddd}
.foot-links{right:176px;top:2391px;display:flex;font-size:13px;color:#ddd}
.foot-links span{padding:0 9px;border-left:1px solid #888;line-height:13px}
.foot-links span:first-child{border-left:0}
.foot-links span:last-child{padding-right:0}
</style>
</head>
<body>

<!-- header -->
<div class="abs brand"><span class="brand-dot"></span><span class="brand-name">Lumen Kinetics™</span></div>
<div class="abs phone">
  <svg width="26" height="26" viewBox="0 0 26 26"><rect x="1" y="4" width="6" height="20" rx="2" fill="#4a4a4a"/><rect x="8" y="2" width="17" height="22" rx="2" fill="#4a4a4a"/><g fill="#fff"><rect x="11" y="5" width="11" height="5"/><rect x="11" y="12" width="3" height="3"/><rect x="15" y="12" width="3" height="3"/><rect x="19" y="12" width="3" height="3"/><rect x="11" y="17" width="3" height="3"/><rect x="15" y="17" width="3" height="3"/><rect x="19" y="17" width="3" height="3"/></g></svg>
  <span>+61 300 555 019</span>
</div>
<nav class="abs nav"><a class="current">Home</a><a>Lumen Kinetics</a><a>About Us</a><a>Articles and Resource</a><a>Contact</a></nav>

<!-- hero -->
<section class="abs hero"></section>
<h1 class="abs hero-title">Consequuntur dolores explicabo nemo voluptem aut natus?</h1>
<p class="abs hero-sub">Aspernatur magni quae aut veritatis beatae eos aut voluptas</p>
<div class="abs video">
  <div class="video-frame" role="img" aria-label="Video still: smiling business team seated at a meeting table"></div>
  <svg class="video-bar" viewBox="0 0 627 46">
    <circle cx="25" cy="23" r="14" fill="#e8e8e8"/><path d="M20 15 L32 23 L20 31Z" fill="#1b1b1b"/>
    <rect x="50" y="20" width="420" height="6" rx="3" fill="#555"/>
    <rect x="50" y="20" width="250" height="6" rx="3" fill="#c0121c"/>
    <circle cx="252" cy="23" r="9" fill="#ddd"/>
    <text x="490" y="28" font-size="13" fill="#ddd" font-family="Arimo,Arial,sans-serif">04:25</text>
    <path d="M535 18 h5 l6 -5 v20 l-6 -5 h-5z" fill="#ddd"/>
    <rect x="556" y="20" width="35" height="6" fill="#555"/><rect x="556" y="20" width="22" height="6" fill="#c0121c"/>
    <g stroke="#ddd" stroke-width="2" fill="none"><path d="M604 16 h-5 v5 M614 16 h5 v5 M604 30 h-5 v-5 M614 30 h5 v-5"/></g>
  </svg>
</div>
<div class="abs stripe" style="left:174px;top:720px"><span class="c1"></span><span class="c2"></span><span class="c3"></span></div>

<!-- features -->
<div class="abs feature" style="left:170px;top:808px">
  <div class="feature-head"><span class="num">1</span><h2 class="feature-title">Programs</h2></div>
  <p>Fugit aut illo omnis explicabo ipsa ipsa, nemo rem ipsam quasi illo dolores ut voluptatem doloremque perspiciatis beatae magni architecto odit odit, aspernatur magni</p>
  <div class="more" style="margin-top:14px">Veritatis unde <svg class="go" viewBox="0 0 14 14"><circle cx="7" cy="7" r="7" fill="#3a3a3a"/><path d="M5.5 4 L8.5 7 L5.5 10" stroke="#fff" stroke-width="1.8" fill="none"/></svg></div>
</div>
<div class="abs feature" style="left:465px;top:808px">
  <div class="feature-head"><span class="num">2</span><h2 class="feature-title">Events</h2></div>
  <p>Voluptas aut sit odit quasi quasi, unde quae ratione inventore ipsa explicabo iste sunt sed ipsam voluptatem consequuntur iste ipsam ipsam consequuntur</p>
  <div class="more" style="margin-top:30px">Sed enim <svg class="go" viewBox="0 0 14 14"><circle cx="7" cy="7" r="7" fill="#3a3a3a"/><path d="M5.5 4 L8.5 7 L5.5 10" stroke="#fff" stroke-width="1.8" fill="none"/></svg></div>
</div>
<div class="abs feature" style="left:758px;top:808px">
  <div class="feature-head"><span class="num">3</span><h2 class="feature-title">Products</h2></div>
  <p>Sed enim accusantium laudantium sunt perspiciatis ipsam sed doloremque ipsam dolores totam unde unde, et aut ill aut veritatis explicabo dicta quia dicta</p>
  <div class="more" style="margin-top:30px">Omnis ipsa <svg class="go" viewBox="0 0 14 14"><circle cx="7" cy="7" r="7" fill="#3a3a3a"/><path d="M5.5 4 L8.5 7 L5.5 10" stroke="#fff" stroke-width="1.8" fill="none"/></svg></div>
</div>

<!-- recent events -->
<div class="abs section-head" style="left:184px;top:986px;width:840px">
  <h2 class="section-title">Recebt events</h2><span class="section-rule"></span>
  <span class="pager"><svg width="34" height="16" viewBox="0 0 34 16"><circle cx="8" cy="8" r="7.5" fill="#3a3a3a"/><path d="M9.5 4.5 L6 8 L9.5 11.5" stroke="#fff" stroke-width="1.8" fill="none"/><circle cx="26" cy="8" r="7.5" fill="#3a3a3a"/><path d="M24.5 4.5 L28 8 L24.5 11.5" stroke="#fff" stroke-width="1.8" fill="none"/></svg></span>
</div>
<div class="abs tabs"><span>Ipsum Voluptatem</span><span>Voluptas Aut Sit</span><span class="on">Quae Ratione</span><span>Perspiciatis Ipsum</span></div>
<div class="abs thumb" style="left:186px;background:linear-gradient(150deg,#e9ecef,#8d949c)" role="img" aria-label="Two colleagues reviewing work at a desk"></div>
<div class="abs thumb" style="left:358px;background:linear-gradient(150deg,#dfe3e8,#5c6168)" role="img" aria-label="Team gathered around a laptop"></div>
<div class="abs thumb" style="left:530px;background:linear-gradient(150deg,#eef0f2,#7d858f)" role="img" aria-label="Group seated in a training session"></div>
<div class="abs thumb" style="left:702px;background:linear-gradient(150deg,#e4e7ea,#6a6f77)" role="img" aria-label="Business people discussing at a table"></div>
<div class="abs thumb" style="left:875px;background:linear-gradient(150deg,#d6dadf,#3f4248)" role="img" aria-label="Smiling team at a meeting"></div>

<!-- training -->
<div class="abs section-head" style="left:184px;top:1256px;width:840px"><h2 class="section-title">Our Training</h2><span class="section-rule"></span></div>

<article class="abs course" style="left:184px;top:1312px">
  <h3 class="course-title">Voluptatem Doloremque</h3>
  <div class="course-meta">April 20, 2013<span class="sep"></span>56 comments<span class="count"><svg width="18" height="13" viewBox="0 0 18 13"><path d="M1 1h10v7H5l-3 3V8H1z" fill="#2a78b6"/><path d="M12 4h5v6h-1v2l-2-2H8V9h4z" fill="#2a78b6"/></svg>56</span></div>
  <div class="course-img" style="background:linear-gradient(160deg,#eef1f4,#5d6a7a)" role="img" aria-label="Business team standing together"></div>
  <p>Nemo rem ipsam quasi illo dolores ut voluptatem doloremque perspiciatis beatae magni architecto odit odit, aspernatur magni</p>
  <div class="more">Veritatis unde <svg class="go" viewBox="0 0 14 14"><circle cx="7" cy="7" r="7" fill="#3a3a3a"/><path d="M5.5 4 L8.5 7 L5.5 10" stroke="#fff" stroke-width="1.8" fill="none"/></svg></div>
</article>
<article class="abs course" style="left:475px;top:1312px">
  <h3 class="course-title">Perspiciatis Beatae</h3>
  <div class="course-meta">April 28, 2013<span class="sep"></span>236 comments<span class="count"><svg width="18" height="13" viewBox="0 0 18 13"><path d="M1 1h10v7H5l-3 3V8H1z" fill="#2a78b6"/><path d="M12 4h5v6h-1v2l-2-2H8V9h4z" fill="#2a78b6"/></svg>236</span></div>
  <div class="course-img" style="background:linear-gradient(160deg,#8a8f96,#3a3c40)" role="img" aria-label="Man working on a laptop"></div>
  <p>Quae ratione inventore ipsa explicabo iste sunt sed ipsam voluptatem consequuntur iste ipsam ipsam consequuntur</p>
  <div class="more" style="margin-top:34px">Sed enim <svg class="go" viewBox="0 0 14 14"><circle cx="7" cy="7" r="7" fill="#3a3a3a"/><path d="M5.5 4 L8.5 7 L5.5 10" stroke="#fff" stroke-width="1.8" fill="none"/></svg></div>
</article>
<article class="abs course" style="left:766px;top:1312px">
  <h3 class="course-title">Veritatis Explicabo</h3>
  <div class="course-meta">April 30, 2013<span class="sep"></span>58 comments<span class="count"><svg width="18" height="13" viewBox="0 0 18 13"><path d="M1 1h10v7H5l-3 3V8H1z" fill="#2a78b6"/><path d="M12 4h5v6h-1v2l-2-2H8V9h4z" fill="#2a78b6"/></svg>58</span></div>
  <div class="course-img" style="position:relative;background:linear-gradient(160deg,#6e5a52,#2e2624)" role="img" aria-label="Team meeting in a dim office">
    <svg style="position:absolute;left:103px;top:34px" width="52" height="52" viewBox="0 0 52 52"><circle cx="26" cy="26" r="26" fill="#1f5f92"/><circle cx="24" cy="24" r="8" stroke="#fff" stroke-width="2.5" fill="none"/><path d="M30 30 L36 36" stroke="#fff" stroke-width="3"/></svg>
  </div>
  <p>Sunt perspiciatis ipsam sed doloremque ipsam dolores totam unde unde, et aut ill aut veritatis explicabo dicta quia dicta</p>
  <div class="more">Omnis ipsa <svg class="go" viewBox="0 0 14 14"><circle cx="7" cy="7" r="7" fill="#3a3a3a"/><path d="M5.5 4 L8.5 7 L5.5 10" stroke="#fff" stroke-width="1.8" fill="none"/></svg></div>
</article>

<!-- experience -->
<div class="abs section-head" style="left:184px;top:1642px;width:264px"><h2 class="section-title">Experience for Yourself</h2><span class="section-rule"></span></div>
<ul class="abs links">
  <li><svg class="go" viewBox="0 0 14 14"><circle cx="7" cy="7" r="7" fill="#1f5f92"/><path d="M5.5 4 L8.5 7 L5.5 10" stroke="#fff" stroke-width="1.8" fill="none"/></svg>Lumen Kinetics for you</li>
  <li><svg class="go" viewBox="0 0 14 14"><circle cx="7" cy="7" r="7" fill="#1f5f92"/><path d="M5.5 4 L8.5 7 L5.5 10" stroke="#fff" stroke-width="1.8" fill="none"/></svg>Lumen Kinetics for Community</li>
  <li><svg class="go" viewBox="0 0 14 14"><circle cx="7" cy="7" r="7" fill="#1f5f92"/><path d="M5.5 4 L8.5 7 L5.5 10" stroke="#fff" stroke-width="1.8" fill="none"/></svg>Lumen Kinetics for Animals</li>
  <li><svg class="go" viewBox="0 0 14 14"><circle cx="7" cy="7" r="7" fill="#1f5f92"/><path d="M5.5 4 L8.5 7 L5.5 10" stroke="#fff" stroke-width="1.8" fill="none"/></svg>Lumen Kinetics for Business</li>
  <li><svg class="go" viewBox="0 0 14 14"><circle cx="7" cy="7" r="7" fill="#1f5f92"/><path d="M5.5 4 L8.5 7 L5.5 10" stroke="#fff" stroke-width="1.8" fill="none"/></svg>Lumen Kinetics for Children<br>and School</li>
  <li><svg class="go" viewBox="0 0 14 14"><circle cx="7" cy="7" r="7" fill="#1f5f92"/><path d="M5.5 4 L8.5 7 L5.5 10" stroke="#fff" stroke-width="1.8" fill="none"/></svg>Became anAccredited<br>Lumen Kinetics Practitioner</li>
</ul>

<!-- testimonials -->
<div class="abs section-head" style="left:500px;top:1642px;width:524px">
  <h2 class="section-title">What They Says</h2><span class="section-rule"></span>
  <span class="pager"><svg width="34" height="16" viewBox="0 0 34 16"><circle cx="8" cy="8" r="7.5" fill="#3a3a3a"/><path d="M9.5 4.5 L6 8 L9.5 11.5" stroke="#fff" stroke-width="1.8" fill="none"/><circle cx="26" cy="8" r="7.5" fill="#3a3a3a"/><path d="M24.5 4.5 L28 8 L24.5 11.5" stroke="#fff" stroke-width="1.8" fill="none"/></svg></span>
</div>
<div class="abs quote" style="left:500px;top:1690px">
  <div class="quote-mark">“</div>
  <p>Voluptas aut sit odit quasi quasi, unde quae ratione inventore ipsa explicabo iste sunt sed ipsam voluptatem consequuntur</p>
</div>
<div class="abs" style="left:500px;top:1840px"><div class="person">Lena Vorst</div><div class="role">Secretary</div></div>
<div class="abs portrait" style="left:649px;top:1806px;background:linear-gradient(160deg,#e9e4e0,#7a5a4c)" role="img" aria-label="Portrait of the client"></div>

<div class="abs quote" style="left:799px;top:1690px">
  <div class="quote-mark">“</div>
  <p>Voluptas aut sit odit quasi quasi, unde quae ratione inventore ipsa explicabo iste sunt sed ipsam voluptatem consequuntur</p>
</div>
<div class="abs" style="left:799px;top:1840px"><div class="person">Tomas Reyna,</div><div class="role">Designer</div></div>
<div class="abs portrait" style="left:935px;top:1806px;background:linear-gradient(160deg,#d8dde3,#4c6a88)" role="img" aria-label="Portrait of the client"></div>

<!-- tweets -->
<div class="abs section-head" style="left:184px;top:1926px;width:840px">
  <h2 class="section-title">Tweet</h2><span class="section-rule"></span>
  <span class="pager"><svg width="34" height="16" viewBox="0 0 34 16"><circle cx="8" cy="8" r="7.5" fill="#3a3a3a"/><path d="M9.5 4.5 L6 8 L9.5 11.5" stroke="#fff" stroke-width="1.8" fill="none"/><circle cx="26" cy="8" r="7.5" fill="#3a3a3a"/><path d="M24.5 4.5 L28 8 L24.5 11.5" stroke="#fff" stroke-width="1.8" fill="none"/></svg></span>
</div>
<div class="abs tweet" style="left:195px;top:1974px"><span class="tweet-dot"></span><div><p><span class="tag">@ unde</span> quasi quae ratione inventore ipsa explicabo iste sunt <span class="tag" style="font-size:10.5px">lnk.example/a7Qz</span></p><div class="date">Mar 1, 2013</div></div></div>
<div class="abs tweet" style="left:498px;top:1974px"><span class="tweet-dot"></span><div><p><span class="tag">@ accusantium</span> laudantium sunt perspiciatis ipsam <span class="tag" style="font-size:10.5px">lnk.example/a7Qz</span></p><div class="date">Mar 4, 2013</div></div></div>
<div class="abs tweet" style="left:776px;top:1974px"><span class="tweet-dot"></span><div><p><span class="tag">@ ratione</span> inventore ipsa explicabo iste sunt sed ipsam voluptatem consequu <span class="tag" style="font-size:10.5px">lnk.example/a7Qz</span></p><div class="date">Mar 10, 2013</div></div></div>

<!-- footer -->
<footer class="abs footer"></footer>
<div class="abs stripe" style="left:174px;top:2093px"><span class="c1"></span><span class="c2"></span><span class="c3"></span></div>

<div class="abs" style="left:205px;top:2145px;width:250px">
  <h3 class="foot-title foot-sans" style="font-size:17px">About Us</h3>
  <p class="foot-text foot-sans" style="margin-top:20px">Amet voluptatem fugit aut illo omnis explicabo ipsa nemo rem ipsam quasi illo dolores ut voluptatem doloremque perspiciatis beatae magni architecto odit</p>
  <div class="foot-row"><svg width="20" height="14" viewBox="0 0 20 14"><rect width="20" height="14" fill="#fff"/><path d="M0 0 L10 8 L20 0" stroke="#2a2828" stroke-width="1.5" fill="none"/></svg>Sign up to our newsletter</div>
  <div class="social" style="margin-top:48px" aria-label="Social profiles"><span></span><span></span><span></span><span></span><span></span></div>
</div>

<div class="abs" style="left:496px;top:2145px;width:230px">
  <h3 class="foot-title">Adreess</h3>
  <div class="foot-row" style="margin-top:22px"><svg width="14" height="20" viewBox="0 0 14 20"><path d="M7 0C3 0 0 3 0 7c0 5 7 13 7 13s7-8 7-13c0-4-3-7-7-7z" fill="#fff"/><circle cx="7" cy="7" r="2.5" fill="#2a2828"/></svg><span>PO BOX<br>Harbour Lane North<br>Vic 3999 Australia</span></div>
  <div class="foot-row"><svg width="14" height="20" viewBox="0 0 14 20"><rect x="2" y="1" width="10" height="18" rx="2" fill="#fff"/><rect x="4" y="4" width="6" height="10" fill="#2a2828"/></svg><span>+61 300 555 019<br>+61 400 555 027</span></div>
  <div class="foot-row"><svg width="14" height="10" viewBox="0 0 14 10"><rect width="14" height="10" fill="#fff"/><path d="M0 0 L7 6 L14 0" stroke="#2a2828" stroke-width="1.3" fill="none"/></svg><span>info@lumenkinetics.example.com</span></div>
</div>

<div class="abs" style="left:772px;top:2145px;width:260px">
  <h3 class="foot-title">Recent Tweets</h3>
  <p class="foot-text" style="margin-top:22px;font-size:13px;line-height:17px">Rationventorene @unde quasi quae audantium beatae ut laudantium. #possum pic.example.com/k4Rt9wQ2<br>Retweeted by Mr. Quill</p>
  <div class="foot-row" style="margin-top:26px;align-items:center">Read More <svg class="go" viewBox="0 0 14 14"><circle cx="7" cy="7" r="7" fill="#fff"/><path d="M5.5 4 L8.5 7 L5.5 10" stroke="#2a2828" stroke-width="1.8" fill="none"/></svg></div>
</div>

<div class="abs foot-rule"></div>
<div class="abs copyright">© 2013 &nbsp; Lumen Kinetics</div>
<div class="abs foot-links"><span>SEO</span><span>Internet Marketing</span><span>Email Marketing</span><span>Web Designs Melbourne</span></div>

</body>
</html>
```